Telmoro Business Card

I already have the conplay logo. I need to develop a professional business card layout

Target Market(s)

Business

Industry/Entity Type

Business

Contact Information for Business Card

Company Name: Telmoro Limited

Font styles to use
Sans Serif

Colors

Designer to choose colors to be used in the design.

Requirements
Must have
• Use current logo
• Need two card size options:
• Small Card: 70mm x 28mm (Landscape)
• Square Card: 65mm x 65mm
Nice to have
• I will need 8-10 files for each name, number and email address (details to follow)

```html
<!DOCTYPE html>
<html lang="en">
<head>
<meta charset="utf-8">
<title>Telmoro Limited – Business Cards</title>
<link href="https://fonts.googleapis.com/css2?family=Arimo:wght@400;700&display=swap" rel="stylesheet">
<style>
  :root {
    --navy: #262b85;
    --name: #3b3f95;
    --orange-text: #f7941d;
    --lime: #dfff98;
    --grey-card: #e6e7e8;
    --white: #ffffff;
    --band-blue: #0d6db7;
    --band-orange: #f39800;
    --band-red: #e6141b;
    --band-yellow: #ffdd00;
    --band-cyan: #29a9e0;
    --band-green: #8cc21f;
    --band-darkgreen: #006b35;
    --wordmark: #1a8a3a;
  }
  * { margin: 0; padding: 0; box-sizing: border-box; }
  html, body { width: 1200px; height: 1155px; overflow: hidden; background: var(--white); }
  body { position: relative; font-family: "Arimo", Arial, sans-serif; }
  .abs { position: absolute; line-height: 1; white-space: nowrap; }

  /* Square striped card */
  .card-striped {
    position: absolute; left: 352px; top: 84px; width: 542px; height: 542px;
    border-radius: 40px; overflow: hidden;
  }
  .band { position: absolute; left: 0; width: 100%; }
  .band--blue { top: 0; height: 70px; background: var(--band-blue); }
  .band--lime { top: 70px; height: 72px; background: var(--lime); }
  .band--orange { top: 142px; height: 70px; background: var(--band-orange); }
  .band--red { top: 212px; height: 72px; background: var(--band-red); }
  .band--yellow { top: 284px; height: 71px; background: var(--band-yellow); }
  .band--cyan { top: 355px; height: 72px; background: var(--band-cyan); }
  .band--green { top: 427px; height: 73px; background: var(--band-green); }
  .band--darkgreen { top: 500px; height: 42px; background: var(--band-darkgreen); }

  .wordmark { font-weight: 700; color: var(--wordmark); letter-spacing: 1px; }
  .company { font-weight: 700; color: var(--navy); }
  .person { font-weight: 700; color: var(--name); letter-spacing: 1px; }
  .role { color: var(--orange-text); }
  .detail { color: var(--navy); }
  .centered { transform: translateX(-50%); text-align: center; }

  .panel-striped {
    position: absolute; left: 377px; top: 314px; width: 495px; height: 254px;
    background: var(--lime); border: 6px solid var(--white); border-radius: 26px;
  }

  /* Grey card */
  .card-grey {
    position: absolute; left: 164px; top: 706px; width: 356px; height: 356px;
    background: var(--grey-card); border-radius: 28px;
  }

  /* Lime card */
  .card-lime {
    position: absolute; left: 706px; top: 706px; width: 356px; height: 356px;
    background: var(--lime); border-radius: 28px;
  }
  .panel-white {
    position: absolute; left: 722px; top: 857px; width: 327px; height: 168px;
    background: var(--white); border-radius: 16px;
  }

  .icon { position: absolute; fill: var(--navy); }
</style>
</head>
<body>

<svg width="0" height="0" style="position:absolute">
  <defs>
    <symbol id="icon-phone" viewBox="0 0 22 30">
      <path d="M14 1 a6 6 0 0 1 6 4" fill="none" stroke="#262b85" stroke-width="1.2"/>
      <path d="M14 3.5 a3.5 3.5 0 0 1 3.5 2.5" fill="none" stroke="#262b85" stroke-width="1.2"/>
      <rect x="13" y="5" width="2" height="6"/>
      <rect x="3" y="9" width="14" height="20" rx="2"/>
      <rect x="5.5" y="11.5" width="9" height="5" fill="#fff"/>
      <g fill="#fff">
        <rect x="5.5" y="19" width="2" height="1.6"/><rect x="9" y="19" width="2" height="1.6"/><rect x="12.5" y="19" width="2" height="1.6"/>
        <rect x="5.5" y="22" width="2" height="1.6"/><rect x="9" y="22" width="2" height="1.6"/><rect x="12.5" y="22" width="2" height="1.6"/>
        <rect x="5.5" y="25" width="2" height="1.6"/><rect x="9" y="25" width="2" height="1.6"/><rect x="12.5" y="25" width="2" height="1.6"/>
      </g>
    </symbol>
    <symbol id="icon-mail" viewBox="0 0 30 20">
      <rect x="1" y="1" width="22" height="15" fill="none" stroke="#262b85" stroke-width="1.6"/>
      <path d="M1 1 L12 10 L23 1" fill="none" stroke="#262b85" stroke-width="1.6"/>
      <circle cx="23" cy="14" r="6" fill="#262b85"/>
      <circle cx="23" cy="14" r="3.8" fill="none" stroke="#fff" stroke-width="1.2"/>
      <circle cx="23" cy="14" r="1.5" fill="none" stroke="#fff" stroke-width="1"/>
    </symbol>
    <symbol id="icon-home" viewBox="0 0 26 24">
      <path d="M13 1 L1 12 L4 12 L4 23 L10 23 L10 16 L16 16 L16 23 L22 23 L22 12 L25 12 Z"/>
      <rect x="18" y="3" width="3" height="6"/>
    </symbol>
  </defs>
</svg>

<!-- Square striped card -->
<div class="card-striped">
  <div class="band band--blue"></div>
  <div class="band band--lime"></div>
  <div class="band band--orange"></div>
  <div class="band band--red"></div>
  <div class="band band--yellow"></div>
  <div class="band band--cyan"></div>
  <div class="band band--green"></div>
  <div class="band band--darkgreen"></div>
</div>
<div class="abs wordmark centered" style="left:623px; top:167px; font-size:47px;">TELMORO</div>
<div class="abs company centered" style="left:623px; top:240px; font-size:42px;">TELMORO LIMITED</div>
<div class="panel-striped"></div>
<div class="abs person" style="left:408px; top:330px; font-size:40px;">ARJUN MEHTA</div>
<div class="abs role" style="left:410px; top:369px; font-size:22px;">Fashion Designer</div>
<svg class="icon" style="left:412px; top:420px;" width="22" height="30"><use href="#icon-phone"/></svg>
<div class="abs detail" style="left:461px; top:424px; font-size:22px;">xx - xxx - xxxxxxx</div>
<svg class="icon" style="left:411px; top:471px;" width="30" height="20"><use href="#icon-mail"/></svg>
<div class="abs detail" style="left:459px; top:457px; font-size:22px;">email@email.com</div>
<svg class="icon" style="left:411px; top:502px;" width="27" height="25"><use href="#icon-home"/></svg>
<div class="abs detail" style="left:458px; top:490px; font-size:22px; line-height:26px;">Address Street 210 Big City<br>Island - Indonesia</div>

<!-- Grey card -->
<div class="card-grey"></div>
<div class="abs wordmark centered" style="left:342px; top:718px; font-size:53px;">TELMORO</div>
<div class="abs company centered" style="left:342px; top:764px; font-size:30px;">TELMORO LIMITED</div>
<div class="abs person centered" style="left:344px; top:849px; font-size:29px;">ARJUN MEHTA</div>
<div class="abs role centered" style="left:343px; top:876px; font-size:16px;">Fashion Designer</div>
<svg class="icon" style="left:332px; top:904px;" width="16" height="23"><use href="#icon-phone"/></svg>
<div class="abs detail centered" style="left:342px; top:935px; font-size:14px;">xx - xxx - xxxxxxx</div>
<svg class="icon" style="left:332px; top:960px;" width="20" height="13"><use href="#icon-mail"/></svg>
<div class="abs detail centered" style="left:342px; top:972px; font-size:16px;">email@email.com</div>
<svg class="icon" style="left:333px; top:997px;" width="18" height="17"><use href="#icon-home"/></svg>
<div class="abs detail centered" style="left:342px; top:1015px; font-size:16px; line-height:17px;">Address Street 210 Big City<br>Island - Indonesia</div>

<!-- Lime card -->
<div class="card-lime"></div>
<div class="abs wordmark centered" style="left:884px; top:737px; font-size:52px;">TELMORO</div>
<div class="abs company centered" style="left:878px; top:786px; font-size:33px;">TELMORO LIMITED</div>
<div class="panel-white"></div>
<div class="abs person" style="left:742px; top:865px; font-size:29px;">ARJUN MEHTA</div>
<div class="abs role" style="left:745px; top:894px; font-size:16px;">Fashion Designer</div>
<svg class="icon" style="left:748px; top:926px;" width="15" height="22"><use href="#icon-phone"/></svg>
<div class="abs detail" style="left:778px; top:929px; font-size:15px;">xx - xxx - xxxxxxx</div>
<svg class="icon" style="left:746px; top:959px;" width="20" height="13"><use href="#icon-mail"/></svg>
<div class="abs detail" style="left:777px; top:952px; font-size:16px;">email@email.com</div>
<svg class="icon" style="left:746px; top:980px;" width="18" height="17"><use href="#icon-home"/></svg>
<div class="abs detail" style="left:776px; top:971px; font-size:16px; line-height:17px;">Address Street 210 Big City<br>Island - Indonesia</div>

</body>
</html>
```